Business Card Design

I need a business card design. I am a sole practitioner.I am a psychotherapist and I need a professional card. I am also an art therapist (a form of psychotherapy using art) so I want the image to be professional/creative/maybe ethnic. I do not want a boring minimalist "medical" image, nor do I want it too hippy/tree hugging.
Colours like reds/ochres/yellows would be good.
Industry/Entity Type
Business
Contact Information for Business Card
Mira Tansen
Psychotherapy, Counselling and Art Therapy
Korrabel Lodge Counselling and Wellbeing services
17 Harlow Lane, Wendmere 4172
0417396025 www.MiraTansen.com.au
on rear of card I need the option to have at least 4 or 5 appointment times /dates
Look and feel
Each slider illustrates characteristics of the customer's brand and the style your logo design should communicate.

```html
<!DOCTYPE html>
<html lang="en">
<head>
<meta charset="utf-8">
<title>Mira Tansen Psychotherapy – Business Card</title>
<link rel="stylesheet" href="https://fonts.googleapis.com/css2?family=Marcellus&family=Open+Sans:wght@400;600&display=swap">
<style>
  :root {
    --backdrop: #3a2a1e;
    --card: #2b2b2b;
    --card-light: #363636;
    --gold: #c08a2a;
    --gold-light: #d9a640;
    --gold-dark: #b07a1c;
    --ink: #1c1408;
    --slot: #ececec;
    --muted: #8a8a8a;
  }
  * { box-sizing: border-box; margin: 0; padding: 0; }
  html, body { width: 1200px; height: 1000px; overflow: hidden; }
  body { background: var(--backdrop); position: relative; }

  .card {
    position: absolute;
    left: 215px;
    width: 770px;
    height: 440px;
    background: linear-gradient(135deg, var(--card-light), var(--card) 60%);
    overflow: hidden;
    box-shadow: 0 10px 30px rgba(0,0,0,.45);
  }
  .card--back { top: 40px; }
  .card--front { top: 520px; }

  .brand { display: flex; align-items: center; gap: 16px; color: var(--gold); }
  .brand__dot {
    width: 44px; height: 44px; border-radius: 50%;
    background: var(--gold);
  }
  .brand__name {
    font-family: "Marcellus", serif;
    font-size: 38px; line-height: 1; letter-spacing: 1px;
  }
  .brand__trade {
    font-family: "Marcellus", serif;
    font-size: 17px; letter-spacing: 5px; margin-top: 4px;
  }

  /* back side */
  .card--back .brand { position: absolute; left: 70px; top: 192px; }
  .divider {
    position: absolute; left: 395px; top: 40px; width: 2px; height: 360px;
    background: var(--gold);
  }
  .appointments { position: absolute; left: 425px; top: 40px; width: 310px; }
  .appointments__title {
    font-family: "Marcellus", serif; color: var(--gold-dark);
    font-size: 15px; letter-spacing: 2px; margin-bottom: 10px;
  }
  .appointments__slot {
    height: 44px; margin-bottom: 22px; background: var(--slot);
    box-shadow: inset 0 2px 6px rgba(0,0,0,.35);
  }

  /* front side */
  .card--front .brand { position: absolute; left: 0; right: 0; top: 52px; justify-content: center; }
  .band {
    position: absolute; left: 0; right: 0; top: 150px; height: 205px;
    background: linear-gradient(90deg, var(--gold-dark), var(--gold) 50%, var(--gold-light));
  }
  .band__rule { position: absolute; left: 0; right: 0; height: 2px; background: var(--ink); }
  .band__rule--top { top: 70px; }
  .band__rule--bottom { top: 150px; }
  .details {
    position: absolute; left: 0; right: 0; text-align: center;
    font-family: "Open Sans", sans-serif; color: var(--ink);
    font-size: 15px; line-height: 1.35; font-weight: 600;
  }
  .details--services { top: 20px; }
  .details--contact { top: 84px; }
  .website {
    position: absolute; left: 0; right: 0; bottom: 34px; text-align: center;
    font-family: "Open Sans", sans-serif; font-size: 13px; color: var(--muted);
  }
</style>
</head>
<body>

<section class="card card--back" aria-label="Card back with appointment slots">
  <div class="brand">
    <span class="brand__dot"></span>
    <div>
      <div class="brand__name">MIRA TANSEN</div>
      <div class="brand__trade">Psychotherapy</div>
    </div>
  </div>
  <div class="divider"></div>
  <div class="appointments">
    <div class="appointments__title">APPOINTMENTS</div>
    <div class="appointments__slot"></div>
    <div class="appointments__slot"></div>
    <div class="appointments__slot"></div>
    <div class="appointments__slot"></div>
    <div class="appointments__slot"></div>
  </div>
</section>

<section class="card card--front" aria-label="Card front with contact details">
  <div class="brand">
    <span class="brand__dot"></span>
    <div>
      <div class="brand__name">MIRA TANSEN</div>
      <div class="brand__trade">Psychotherapy</div>
    </div>
  </div>
  <div class="band">
    <p class="details details--services">Counselling and Art Therapy<br>Korrabel Lodge Counselling and Wellbeing services</p>
    <div class="band__rule band__rule--top"></div>
    <p class="details details--contact">17 Harlow Lane, Wendmere 4172<br>tel: 0417396025</p>
    <div class="band__rule band__rule--bottom"></div>
  </div>
  <p class="website">www.MiraTansen.com.au</p>
</section>

</body>
</html>
```